Branding Guide and Website for Q7Systems

Need an experienced Graphics Designer with a proven track record to create a design and branding guide for all media formats. From this guide you will then create a new website design for Q7systems.com.
There will be 8 pages (to start) with the new website. Each page will have multiple features and panels each need to have individual attention and customization that collectively fit together into a single cohesive look and feel.
We have not been able to get good designs I’m attaching one version which is the best we’ve received which is not bad but needs to be polished up better and the images need to change. I’d like to have some other accent colors but not too much I like the white, dark blue, gray, dark gray style.
Here are some sites that I like –
http://www.varnelo.com/
https://www.probrantix.com/ (layout good, graphics not great)
http://www.dusketal.com/ (good layout and graphics, too much animation)
https://www.pavemundo.com/ (a little boring but the colors and some of the top images are good)
https://www.torquidell.com/ (a little over the top colors are off but they have some good info graphics)
We don’t expect you will code the site however if you have that capability we’ll need it responsive/flat for mobile. Otherwise we can find someone to do the programming and we’ll just need the design files and images.
Branding guide will be used for web, email, print etc. so you’ll need to consider all guidelines for all formats. That is about it let me know if any questions we can have a call to discuss further if it is easier.
Not sure why they want a minimum of 300 words I’m done now but apparently have to keep typing so that is what I’m doing and Ok I’m at 300 words, almost there and we’re here now.

Target Market(s)

Customers looking for IT Services, Private Cloud, Security Services, Advanced Support, Fully Managed or Co-Managed IT.

Industry/Entity Type

It Company

Number of Pages Required

5+ page

Font styles to use
Sans Serif

Colors
0255a3
959595
e6e6e6
ffffff

Requirements
Must have
• Clean, professional and modern look using iconography, info graphics, flat etc.

```html
<!DOCTYPE html>
<html lang="en">
<head>
<meta charset="utf-8">
<title>Q7Systems – IT Service Excellence</title>
<link rel="stylesheet" href="https://fonts.googleapis.com/css2?family=Open+Sans:wght@300;400;600;700&display=swap">
<style>
:root{
  --brand:#0255a3;
  --brand-dark:#013a74;
  --brand-deep:#021d3e;
  --grey:#959595;
  --grey-dark:#4a4a4a;
  --grey-light:#e6e6e6;
  --panel:#f3f4f6;
  --white:#ffffff;
}
*{box-sizing:border-box;margin:0;padding:0}
html,body{width:1200px;height:2468px;overflow:hidden}
body{font-family:"Open Sans",Arial,sans-serif;color:var(--grey-dark);background:var(--white)}
a{color:inherit;text-decoration:none}

/* Header */
.site-header{height:120px;display:flex;align-items:center;justify-content:space-between;padding:0 40px 0 44px;background:var(--white);border-bottom:1px solid var(--grey-light)}
.brand{display:flex;align-items:center;gap:10px;font-size:30px;font-weight:700;color:var(--brand)}
.brand-mark{width:14px;height:14px;background:var(--brand)}
.main-nav{display:flex;align-items:center;gap:34px}
.main-nav a{font-size:13px;line-height:16px;color:var(--grey);text-align:center;width:92px}
.main-nav a.is-active{color:var(--brand);font-weight:600}
.menu-toggle{width:38px;height:38px;border:1px solid var(--grey-light);display:flex;flex-direction:column;justify-content:center;align-items:center;gap:5px}
.menu-toggle span{width:18px;height:2px;background:var(--grey)}

/* Hero */
.hero{position:relative;height:440px;background:linear-gradient(100deg,#04142c 0%,#062a57 45%,#0b4f96 100%);overflow:hidden}
.hero-visual{position:absolute;left:90px;top:40px;width:420px;height:360px;border-radius:50%;background:radial-gradient(circle at 50% 45%,rgba(140,200,255,.75) 0%,rgba(60,140,230,.35) 35%,rgba(4,20,44,0) 70%)}
.hero-copy{position:absolute;right:110px;top:165px;text-align:right;color:var(--white)}
.hero-copy h1{font-size:46px;font-weight:400;letter-spacing:.5px}
.hero-copy p{margin-top:10px;font-size:14px;color:#cfe0f3;border-top:1px solid rgba(255,255,255,.4);padding-top:8px;display:inline-block}
.hero-arrow{position:absolute;top:200px;width:30px;height:40px}
.hero-arrow.prev{left:20px}
.hero-arrow.next{right:20px}

/* Section headings */
.section-title{font-size:46px;font-weight:300;text-align:center;color:var(--brand)}
.section-lede{font-size:17px;text-align:center;max-width:760px;margin:10px auto 0;line-height:26px;color:var(--grey-dark)}

/* What we do – services */
.services{height:440px;padding-top:38px}
.service-cards{display:flex;gap:20px;width:1000px;margin:34px auto 0}
.service-card{width:184px;height:196px;background:var(--panel);padding:20px 16px}
.service-card .icon{width:30px;height:30px;margin-bottom:12px}
.service-card h3{font-size:14px;line-height:18px;font-weight:700;color:var(--brand);text-transform:uppercase}
.service-card p{margin-top:10px;font-size:11px;line-height:16px;color:var(--grey)}
.service-stats{display:flex;gap:20px;width:1000px;margin:10px auto 0}
.service-stats span{width:184px;font-size:28px;font-weight:300;color:#b4b4b4}

/* What we do – coverage band */
.coverage{position:relative;height:460px;padding-top:38px;background:linear-gradient(120deg,#023f80 0%,var(--brand) 50%,#0b6bc6 100%);color:var(--white);overflow:hidden}
.coverage .section-title,.coverage .section-lede{color:var(--white)}
.coverage-curves{position:absolute;inset:0}
.coverage-grid{position:relative;display:grid;grid-template-columns:420px 420px;gap:44px 60px;width:900px;margin:46px auto 0}
.coverage-item{display:flex;gap:18px}
.coverage-item .badge{flex:none;width:60px;height:60px;border-radius:50%;background:var(--white);display:flex;align-items:center;justify-content:center}
.coverage-item h3{font-size:23px;font-weight:400}
.coverage-item p{margin-top:6px;font-size:11px;line-height:17px;color:#d6e6f7}

/* We are different */
.difference{height:540px;padding-top:38px}
.difference-cols{display:flex;gap:48px;width:1000px;margin:26px auto 0}
.difference-col{width:301px}
.difference-col h3{font-size:30px;font-weight:300;color:var(--brand);margin-bottom:14px}
.difference-photo{height:140px}
.difference-col p{margin-top:14px;font-size:11px;line-height:18px;color:var(--grey)}

/* Results */
.results{height:260px;padding-top:26px;background:linear-gradient(180deg,#c9d3de 0%,#e6e6e6 100%)}
.results .section-title{color:#25364a;font-size:40px}
.results-row{display:flex;gap:20px;width:1000px;margin:22px auto 0}
.result{width:235px}
.result-photo{height:106px}
.result figcaption{background:var(--brand);color:var(--white);font-size:11px;padding:6px 10px}

/* Footer */
.site-footer{height:208px;display:flex;gap:60px;padding:36px 100px 0;background:var(--white);border-top:1px solid var(--grey-light)}
.footer-brand{width:300px}
.footer-brand .brand{font-size:24px}
.footer-brand p{margin-top:12px;font-size:11px;line-height:17px;color:var(--grey)}
.footer-col{width:170px}
.footer-col h4{font-size:12px;font-weight:600;color:var(--brand);margin-bottom:10px}
.footer-col li{list-style:none;font-size:11px;line-height:19px;color:var(--grey);display:flex;align-items:center;gap:6px}
.footer-col li i{width:8px;height:8px;background:var(--grey-light);display:inline-block}
</style>
</head>
<body>

<header class="site-header">
  <a class="brand" href="#"><span class="brand-mark"></span>Q7Systems</a>
  <nav class="main-nav">
    <a class="is-active" href="#">Managed<br>Services</a>
    <a href="#">IT/Private<br>Cloud</a>
    <a href="#">Network<br>Services</a>
    <a href="#">Disaster<br>Recovery</a>
    <a href="#">Services</a>
    <a href="#">Company</a>
    <span class="menu-toggle"><span></span><span></span><span></span></span>
  </nav>
</header>

<section class="hero">
  <div class="hero-visual" role="img" aria-label="Open hand holding a glowing network cube"></div>
  <div class="hero-copy">
    <h1>IT Service Excellence</h1>
    <p>Striving for Continuous Service Improvement for our Clients</p>
  </div>
  <svg class="hero-arrow prev" viewBox="0 0 30 40"><polyline points="20,8 8,20 20,32" fill="none" stroke="#fff" stroke-width="3"/></svg>
  <svg class="hero-arrow next" viewBox="0 0 30 40"><polyline points="10,8 22,20 10,32" fill="none" stroke="#fff" stroke-width="3"/></svg>
</section>

<section class="services">
  <h2 class="section-title">What we do</h2>
  <p class="section-lede">'White Glove' Information Technology Services that ensure our clients are able to focus on their business rather than the IT business.</p>
  <div class="service-cards">
    <article class="service-card">
      <svg class="icon" viewBox="0 0 30 30"><rect x="4" y="4" width="22" height="8" fill="#0255a3"/><rect x="4" y="16" width="22" height="8" fill="#0255a3"/></svg>
      <h3>Managed<br>Services</h3>
      <p>Fully managed or co-managed IT support with proactive monitoring and helpdesk.</p>
    </article>
    <article class="service-card">
      <svg class="icon" viewBox="0 0 30 30"><path d="M8 22h15a5 5 0 0 0 0-10 7 7 0 0 0-13-1 5 5 0 0 0-2 11z" fill="#0255a3"/></svg>
      <h3>Private<br>Cloud</h3>
      <p>Dedicated private cloud hosting with secure storage and flexible scaling.</p>
    </article>
    <article class="service-card">
      <svg class="icon" viewBox="0 0 30 30"><circle cx="15" cy="15" r="11" fill="none" stroke="#0255a3" stroke-width="3"/><path d="M4 15h22M15 4v22" stroke="#0255a3" stroke-width="2"/></svg>
      <h3>Network<br>Services</h3>
      <p>Design, installation and upkeep of fast and reliable business networks.</p>
    </article>
    <article class="service-card">
      <svg class="icon" viewBox="0 0 30 30"><path d="M15 5a10 10 0 1 1-10 10" fill="none" stroke="#0255a3" stroke-width="3"/><polygon points="2,12 8,12 5,18" fill="#0255a3"/></svg>
      <h3>Disaster<br>Recovery</h3>
      <p>Backup and recovery plans that restore your systems within hours.</p>
    </article>
    <article class="service-card">
      <svg class="icon" viewBox="0 0 30 30"><path d="M15 3l10 4v7c0 7-5 11-10 13C10 25 5 21 5 14V7z" fill="#0255a3"/></svg>
      <h3>Security<br>Services</h3>
      <p>Threat protection, audits and firewall care to keep your data safe.</p>
    </article>
  </div>
  <div class="service-stats">
    <span>24/7 Support</span><span>99.9% Uptime</span><span>1st Class</span><span>4hr RTO</span><span>4hr RTO</span>
  </div>
</section>

<section class="coverage">
  <svg class="coverage-curves" viewBox="0 0 1200 460" preserveAspectRatio="none"><path d="M0 380 C300 300 700 460 1200 330" fill="none" stroke="rgba(255,255,255,.12)" stroke-width="2"/><path d="M0 420 C400 340 800 470 1200 380" fill="none" stroke="rgba(255,255,255,.08)" stroke-width="2"/></svg>
  <h2 class="section-title">What we do</h2>
  <p class="section-lede">'White Glove' Information Technology Services that ensure our clients are able to focus on their business rather than the IT business.</p>
  <div class="coverage-grid">
    <div class="coverage-item">
      <span class="badge"><svg width="30" height="30" viewBox="0 0 30 30"><circle cx="15" cy="6" r="4" fill="#0255a3"/><circle cx="6" cy="24" r="4" fill="#0255a3"/><circle cx="24" cy="24" r="4" fill="#0255a3"/><path d="M15 6L6 24M15 6l9 18M6 24h18" stroke="#0255a3" stroke-width="2"/></svg></span>
      <div><h3>Your Network</h3><p>We monitor, patch and tune every switch, router and link so your team always stays connected and productive.</p></div>
    </div>
    <div class="coverage-item">
      <span class="badge"><svg width="30" height="30" viewBox="0 0 30 30"><rect x="6" y="4" width="18" height="6" fill="#0255a3"/><rect x="6" y="12" width="18" height="6" fill="#0255a3"/><rect x="6" y="20" width="18" height="6" fill="#0255a3"/></svg></span>
      <div><h3>Your Servers and Applications</h3><p>From hardware to cloud platforms, we keep servers and business applications running, updated and backed up.</p></div>
    </div>
    <div class="coverage-item">
      <span class="badge"><svg width="30" height="30" viewBox="0 0 30 30"><rect x="4" y="6" width="22" height="15" fill="none" stroke="#0255a3" stroke-width="3"/><path d="M10 25h10" stroke="#0255a3" stroke-width="3"/></svg></span>
      <div><h3>Your Web Presence</h3><p>Hosting, domains and email handled with care so customers can reach you any time, on any device.</p></div>
    </div>
    <div class="coverage-item">
      <span class="badge"><svg width="30" height="30" viewBox="0 0 30 30"><path d="M8 20a7 7 0 1 1 14 0z" fill="#0255a3"/><circle cx="15" cy="9" r="4" fill="#0255a3"/></svg></span>
      <div><h3>Your Piece of Mind</h3><p>A single trusted partner watching over your technology, so you can focus fully on growing your business.</p></div>
    </div>
  </div>
</section>

<section class="difference">
  <h2 class="section-title">We are different</h2>
  <div class="difference-cols">
    <div class="difference-col">
      <h3>Culture</h3>
      <div class="difference-photo" role="img" aria-label="Hand pressing a service bubble on a blue screen" style="background:linear-gradient(135deg,#9bb6d2,#e6ecf2)"></div>
      <p>Our people are driven by service first. We listen, we respond quickly and we treat your business as if it were our own, every single day.</p>
    </div>
    <div class="difference-col">
      <h3>Goals</h3>
      <div class="difference-photo" role="img" aria-label="Server racks in a dimly lit data centre" style="background:linear-gradient(135deg,#1c2c44,#5d7796)"></div>
      <p>Our goal is simple: stable systems, fewer outages and clear reporting. We measure our success by the uptime and satisfaction of every client.</p>
    </div>
    <div class="difference-col">
      <h3>One Partner</h3>
      <div class="difference-photo" role="img" aria-label="Business handshake in an office" style="background:linear-gradient(135deg,#cfd6de,#8c9aa8)"></div>
      <p>One partner for support, cloud, network and security. One call resolves your issue, with a team that already knows your environment well.</p>
    </div>
  </div>
</section>

<section class="results">
  <h2 class="section-title">Unsurpassed Results</h2>
  <div class="results-row">
    <figure class="result"><div class="result-photo" role="img" aria-label="Climbers reaching a mountain summit at sunset" style="background:linear-gradient(135deg,#2d4a6e,#d49b5a)"></div><figcaption>Faster response times</figcaption></figure>
    <figure class="result"><div class="result-photo" role="img" aria-label="Glowing blue network globe" style="background:linear-gradient(135deg,#06224a,#2a77c9)"></div><figcaption>Reliable global access</figcaption></figure>
    <figure class="result"><div class="result-photo" role="img" aria-label="Team working at laptops" style="background:linear-gradient(135deg,#a5b3c2,#e0e4e8)"></div><figcaption>Happier productive teams</figcaption></figure>
    <figure class="result"><div class="result-photo" role="img" aria-label="Close view of a network switch with cables" style="background:linear-gradient(135deg,#1a1f27,#6d7a88)"></div><figcaption>Secure modern systems</figcaption></figure>
  </div>
</section>

<footer class="site-footer">
  <div class="footer-brand">
    <a class="brand" href="#"><span class="brand-mark"></span>Q7Systems</a>
    <p>Copyright © 2024 Q7Systems Inc.<br>All Rights Reserved.<br>Privacy Policy</p>
  </div>
  <div class="footer-col">
    <h4>Browse</h4>
    <ul><li>Managed Services</li><li>IT/Private Cloud</li><li>Network Services</li><li>Disaster Recovery</li><li>Security</li></ul>
  </div>
  <div class="footer-col">
    <h4>Connect</h4>
    <ul><li><i></i>Newsroom</li><li><i></i>Community</li><li><i></i>Updates</li><li><i></i>Events</li></ul>
  </div>
  <div class="footer-col">
    <h4>Contact Us</h4>
    <ul><li>4120 Harbor Point Road</li><li>Suite 210, Brookvale</li><li>(555) 014-2280</li><li>info@q7systems.com</li></ul>
  </div>
</footer>

</body>
</html>
```